Oil Field Service company needs professional business cards

Looking to clean up our current company business cards and look a little more professional. Harlow Tubular Services is a US based company that services the oil field. We deal with engineers, managers and oil rigs....................................................................................................................................................................................................................................................................................................................................................................................................

Target Market(s)

Oil and Gas professionals

Industry/Entity Type

Oil And Gas

Contact Information for Business Card

See attached photo as example

Font styles to use
Sans Serif

Colors
ec1f27

Requirements
Must have
• Company Logo, Name, Title, Cell, Office, Fax, Email.
• See attached photo
Nice to have
• External CRT, Internal CRT, Casing Crews, Torque Turn, Laydown Machine
Should not have
• Do not introduce any new pictures and keep it professional looking

```html
<!DOCTYPE html>
<html lang="en">
<head>
<meta charset="utf-8">
<title>Harlow Tubular Services – Business Card</title>
<link href="https://fonts.googleapis.com/css2?family=Open+Sans:wght@300;400;600;700&display=swap" rel="stylesheet">
<style>
  :root {
    --stage: #1c1c1d;
    --card-white: #ffffff;
    --card-dark: #353839;
    --brand-red: #ec1f27;
    --ink-navy: #1f3f4f;
    --ink-gray: #4a4f52;
    --on-dark: #e4e6e7;
  }
  * { margin: 0; padding: 0; box-sizing: border-box; }
  html, body {
    width: 1200px; height: 1000px; overflow: hidden;
    background: var(--stage);
    font-family: "Open Sans", Arial, sans-serif;
  }
  .business-card {
    position: absolute; left: 162px; top: 250px;
    width: 875px; height: 500px;
    border-radius: 42px; overflow: hidden;
    background: var(--card-white);
  }
  .card-swoosh { position: absolute; inset: 0; }
  .company-block {
    position: absolute; right: 70px; top: 50px; text-align: right;
  }
  .company-name {
    font-weight: 700; font-size: 40px; letter-spacing: 1px;
    color: var(--ink-gray); line-height: 1;
  }
  .company-sub {
    font-weight: 700; font-size: 15px; letter-spacing: 2px;
    color: var(--ink-gray); margin-top: 6px;
  }
  .company-address {
    font-size: 17px; color: var(--ink-gray); margin-top: 4px;
  }
  .holder {
    position: absolute; left: 82px; top: 225px;
  }
  .holder-name {
    font-weight: 700; font-size: 30px; color: var(--ink-navy); line-height: 1.1;
  }
  .holder-title {
    font-weight: 400; font-size: 26px; color: var(--brand-red); line-height: 1.15;
  }
  .services {
    position: absolute; right: 55px; top: 275px;
    list-style: none; text-align: right;
    color: var(--on-dark); font-weight: 300; font-size: 20px; line-height: 1.25;
  }
  .contacts {
    position: absolute; left: 70px; top: 385px;
    list-style: none; color: var(--on-dark);
    font-weight: 300; font-size: 20px; line-height: 1.25;
  }
  .contacts li { display: flex; align-items: center; gap: 18px; }
  .contacts svg { width: 16px; height: 16px; fill: var(--on-dark); flex: none; }
</style>
</head>
<body>
  <div class="business-card">
    <svg class="card-swoosh" viewBox="0 0 875 500" preserveAspectRatio="none" aria-hidden="true">
      <path fill="var(--brand-red)" d="M0,352 C300,325 600,270 875,195 L875,212 C600,290 300,345 0,366 Z"/>
      <path fill="var(--card-dark)" d="M0,366 C300,345 600,290 875,212 L875,500 L0,500 Z"/>
    </svg>

    <div class="company-block">
      <div class="company-name">HARLOW</div>
      <div class="company-sub">TUBULAR SERVICES</div>
      <div class="company-address">Redfield, OK 73990</div>
    </div>

    <div class="holder">
      <div class="holder-name">CASEY BRANDT</div>
      <div class="holder-title">AREA MANAGER</div>
    </div>

    <ul class="services">
      <li>Laydown Machine</li>
      <li>Casing Crew</li>
      <li>Mud Tools</li>
      <li>Torque Turn</li>
    </ul>

    <ul class="contacts">
      <li>
        <svg viewBox="0 0 16 16" aria-label="Cell"><path d="M4 0h8a1 1 0 0 1 1 1v14a1 1 0 0 1-1 1H4a1 1 0 0 1-1-1V1a1 1 0 0 1 1-1zm1 2v10h6V2z"/></svg>
        <span>(555) 214 6800</span>
      </li>
      <li>
        <svg viewBox="0 0 16 16" aria-label="Office"><path d="M3.6 1l2.6 3-1.6 2c.9 2 2.4 3.5 4.4 4.4l2-1.6 3 2.6-1.6 2.6C7.3 15 1 8.7 1 2.6z"/></svg>
        <span>(555) 381 4927</span>
      </li>
      <li>
        <svg viewBox="0 0 16 16" aria-label="Fax"><path d="M4 1h6l2 2v3H4zM2 7h12a1 1 0 0 1 1 1v6a1 1 0 0 1-1 1H2a1 1 0 0 1-1-1V8a1 1 0 0 1 1-1zm2 3v2h2v-2zm4 0v2h4v-2z"/></svg>
        <span>(555) 214 6833</span>
      </li>
      <li>
        <svg viewBox="0 0 16 16" aria-label="Email"><path d="M1 3h14v1L8 9 1 4zm0 3l7 5 7-5v7H1z"/></svg>
        <span>cbrandt@harlowtubular.com</span>
      </li>
    </ul>
  </div>
</body>
</html>
```